Book Cover for book, "Lanterns Beyond Marrowfield"

My 6" X 9" book cover (plus bleeds, spine and back cover [no artwork needed for back cover, but would like same color scheme there {will have descriptive text box added to back cover later}]) needs to show American patriotic theme, where the government has gone at least some awry (where members of Congress and federal officials ignore their duty to support the U.S. Constitution within the Constitution's express parameters, and do as they please [mostly to enrich themselves]).

Target Market(s)

Conservative/libertarian/constitutional patriotic (Christian) Americans.
Bible-believing gun owners, etc.

Industry/Entity Type

Political

Font styles to use
Serif

Requirements
Must have
• Some iconic symbol of American liberty and freedom, perhaps now flawed in some way (Statue of Liberty crying or behind bars in jail, the Constitution/Bill of Rights being intentionally torn or shredded, the blindfolded Lady Justice with uneven scales, a sickened Bald Eagle, Gold and Silver COIN (not bars) being replaced with paper currency, Uncle Sam crying or something similar).
Nice to have
• The book title (Lanterns Beyond Marrowfield) and the author (Jonas Perrault) should have either the text in a separate layer or a separate file (one file with artwork and another file with artwork and text).
• The book spine will be thin, probably less than 3/16", so probably no text on spine.
• Patriotic colors (Red, white and blue) are fine, but need not be if the artwork would conflict with them.
Should not have
• Nothing that reminds viewers of Antifa-type of anarchistic disrespectful behavior. No rioting, picketing, etc.
• Should not show the American Flag being disrespected.

```html
<!DOCTYPE html>
<html lang="en">
<head>
<meta charset="utf-8">
<title>Lanterns Beyond Marrowfield — Book Cover</title>
<link rel="stylesheet" href="https://fonts.googleapis.com/css2?family=Bebas+Neue&family=Roboto+Condensed:wght@400;700&display=swap">
<style>
  :root {
    --cover-red: #c8191f;
    --stripe-red: #d3202a;
    --liberty-blue: #0055a5;
    --statue-blue: #1f6fc1;
    --statue-deep: #0d2a55;
    --paper: #ffffff;
    --ink: #111111;
  }
  html, body {
    margin: 0;
    padding: 0;
    width: 1200px;
    height: 1200px;
    overflow: hidden;
    background: var(--paper);
  }
  .canvas {
    position: relative;
    width: 1200px;
    height: 1200px;
  }
  .back-cover {
    position: absolute;
    left: 35px;
    top: 179px;
    width: 576px;
    height: 862px;
    background: var(--cover-red);
  }
  .back-title {
    position: absolute;
    left: 0;
    top: 0;
    width: 576px;
    height: 400px;
  }
  .back-title text {
    font-family: "Bebas Neue", sans-serif;
    fill: var(--paper);
    text-anchor: middle;
  }
  .back-blurb {
    position: absolute;
    left: 86px;
    top: 224px;
    width: 403px;
    height: 440px;
    overflow: hidden;
    color: var(--paper);
    font-family: "Roboto Condensed", sans-serif;
    font-size: 12.5px;
    line-height: 19.3px;
    text-align: justify;
  }
  .back-blurb p { margin: 0 0 19.3px; }

  .front-cover {
    position: absolute;
    left: 611px;
    top: 179px;
    width: 574px;
    height: 862px;
    background: var(--paper);
  }
  .front-art {
    position: absolute;
    left: 0;
    top: 0;
    width: 574px;
    height: 862px;
  }
  .statue-art {
    position: absolute;
    left: 62px;
    top: 328px;
    width: 394px;
    height: 534px;
    background: linear-gradient(160deg, var(--statue-blue) 0%, #0f4f9a 60%, var(--statue-deep) 100%);
    border-radius: 120px 160px 0 0;
  }
  .front-title {
    position: absolute;
    left: 0;
    top: 0;
    width: 574px;
    height: 440px;
  }
  .front-title text {
    font-family: "Bebas Neue", sans-serif;
    text-anchor: middle;
  }
  .title-small { fill: var(--liberty-blue); }
  .title-large { fill: var(--cover-red); }
  .author-name {
    font-family: "Roboto Condensed", sans-serif;
    font-weight: 700;
    fill: var(--ink);
    text-anchor: middle;
  }
</style>
</head>
<body>
<main class="canvas">

  <section class="back-cover">
    <svg class="back-title" viewBox="0 0 576 400" aria-label="Lanterns Beyond Marrowfield">
      <text x="288" y="74" font-size="47">LANTERNS</text>
      <text x="288" y="141" font-size="86">BEYOND</text>
      <text x="288" y="201" font-size="66">MARROWFIELD</text>
    </svg>
    <div class="back-blurb">
      <p>When sworn officials set aside the limits written into the Constitution, the republic does not fall in a single day. It erodes quietly, one unchecked spending bill and one ignored boundary at a time. This book traces how the federal government drifted from its enumerated powers, who benefits from that drift, and why ordinary citizens have carried the cost in lost liberty, shrinking savings, and fading trust in the institutions meant to serve them.</p>
      <p>Drawing on the founding documents, the debates of the ratifying conventions, and the plain words of the framers, the author sets out what the national government was designed to do and what it was never permitted to touch. Each chapter compares that original charter with the present record of Congress and the agencies, showing where oaths were kept, where they were bent, and where they were simply forgotten for personal gain.</p>
      <p>Written for every citizen who still reads the Bill of Rights as a promise, this is a sober and hopeful guide. It offers no slogans and no anger, only history, evidence, and a clear path toward holding elected servants to the oath they swore before God and the nation.</p>
    </div>
  </section>

  <section class="front-cover">
    <svg class="front-art" viewBox="0 0 574 862">
      <defs>
        <clipPath id="stripe-field">
          <rect x="189" y="321" width="357" height="401"/>
        </clipPath>
      </defs>
      <g class="flag-stripes" clip-path="url(#stripe-field)" fill="var(--stripe-red)">
        <polygon points="120,722 160,722 600,282 560,282"/>
        <polygon points="230,762 270,762 650,382 610,382"/>
        <polygon points="330,782 370,782 700,452 660,452"/>
        <polygon points="430,802 470,802 760,512 720,512"/>
        <polygon points="520,812 560,812 820,552 780,552"/>
      </g>
      <rect class="blue-band" x="109" y="722" width="465" height="140" fill="var(--liberty-blue)"/>
    </svg>

    <div class="statue-art" role="img" aria-label="Illustration of the Statue of Liberty raising her torch, in shades of blue"></div>

    <svg class="front-title" viewBox="0 0 574 440" aria-label="Lanterns Beyond Marrowfield by Jonas Perrault">
      <text class="title-small" x="287" y="81" font-size="86">LANTERNS</text>
      <text class="title-large" x="287" y="214" font-size="180">BEYOND</text>
      <text class="title-small" x="287" y="325" font-size="112">MARROWFIELD</text>
      <text class="author-name" x="303" y="424" font-size="36">JONAS PERRAULT</text>
    </svg>
  </section>

</main>
</body>
</html>
```